Brisk Plumes Informational brochure

Creative and attractive brochure with product information, instructions, and self care.

Brisk Plumes:
We are a cannabis vape company located in California. Our vape cartridges are pre-filled with our award winning oil for the most discreet and convenient way for patients to medicate.

-The brochure/ informational card will have the same similar design/ scheme as the product packaging.

Content:

---------------------
"Brisk Plumes

Unlike many other extraction processes, our oil is SOLVENT-FREE with absolutely NO additives or harmful chemicals. All of our extractions are strain specific and lab tested for potency, residuals, and most importantly CONSISTENCY.

Our vapes are specifically designed to be discreet yet incredibly effective for everyday use.

It's simple. NO butane, NO glycol, NO glycerin. Just pure cannabis oil made in California"

"Voted Best Oil at 2015 Leafmoot in San Bernardino and San Francisco"

---------------------
KNOW THE DIFFERENCE

Butane is a highly volatile and flammable gas used for cannabis extractions also known as "BHO" extractions very popular in today's industry. These extractions are not only dangerous, but also contain chemical contaminants that could present health hazards and cause harmful nodules in the lungs that increase chances of getting infections. When done improperly, harmful chemical solvents are left over for the consumers to smoke, which can cause detrimental long-term health effects.

---------------------
"WHAT IS THC?

THC, or "tetrahydrocannabinol," is the chemical responsible for most of marijuana's psychological effects. It acts much like the cannabinoid chemicals made naturally by the body.

Cannabinoid receptors are concentrated in certain areas of the brain associated with thinking, memory, pleasure, coordination, and time perception. THC attaches to these receptors and activates them.

THC is one of many compounds found in the resin secreted by glands of the marijuana plant. More of these glands are found around the reproductive organs of the plant than on any other area of the plant. Other compounds unique to marijuana, called cannabinoids, are present in this resin. One cannabinoid, CBD is non-psychoactive and actually blocks the high associated with THC.

WHAT IS CBD?

CBD is one of over 60 compounds found in cannabis that belongs to a class of molecules called "cannabinoids." CBD from cannabis is non-psychoactive or less psychoactive than THC-dominant strains, making it an appealing option for patients looking for relief from inflammation, pain, anxiety, psychosis, seizures, spasms, and other conditions without disconcerting feelings of lethargy or dysphoria. CBD has demonstrable neuroprotective and neurogenic effects, and its anti-cancer properties are currently being investigated at several academic research centers in the United States and elsewhere."
---------------------

"Cleaning & Care

Store vape cartridges flat or upright in cool or room temperature to prevent leakage. Exposure to excessive heat may cause the viscosity of the oil to change.

Please refer to our Clipstream (https://lnk.example-short.test/Qp7RmZ) page for videos on proper storage and refill instructions!

Instagram logo with ID:
BriskPlume_

Facebook logo with ID
BriskPlumesProducts

Email:
contact@briskplume-mail.test

Clipstream
Brisk Plume (https://lnk.example-short.test/Qp7RmZ)

```html
<!DOCTYPE html>
<html lang="en">
<head>
<meta charset="utf-8">
<title>Brisk Plumes – Informational Brochure</title>
<link href="https://fonts.googleapis.com/css2?family=Montserrat:wght@600;700&family=Quicksand:wght@500;600&display=swap" rel="stylesheet">
<style>
  :root {
    --magenta: #d6005a;
    --white: #ffffff;
    --ink: #3a3a3a;
    --stage: #dfe4e6;
    --faint: rgba(244, 196, 214, 0.4);
    --faint-on-pink: rgba(255, 150, 185, 0.28);
  }
  * { margin: 0; padding: 0; box-sizing: border-box; }
  html, body { width: 1200px; height: 1200px; overflow: hidden; }
  body { background: var(--stage); position: relative; font-family: "Quicksand", sans-serif; }

  .page {
    position: absolute;
    width: 492px;
    height: 695px;
    background: var(--white);
    overflow: hidden;
    transform: scale(0.8);
    transform-origin: 0 0;
  }
  .page--front { left: 174px; top: 300px; }
  .page--back { left: 674px; top: 299px; height: 697px; }

  .shape { position: absolute; left: 0; top: 0; width: 100%; height: 100%; }

  .brand {
    position: absolute;
    left: 0; width: 100%;
    text-align: center;
    font-family: "Montserrat", sans-serif;
    font-weight: 700;
    color: var(--magenta);
    font-size: 34px;
    letter-spacing: 0.5px;
  }
  .brand__dot {
    display: block;
    width: 34px; height: 34px;
    border-radius: 50%;
    background: var(--magenta);
    margin: 0 auto 10px;
  }

  .copy {
    position: absolute;
    font-size: 7.4px;
    line-height: 10px;
    font-weight: 600;
    z-index: 1;
  }
  .copy p + p { margin-top: 10px; }
  .copy--light { color: var(--white); }
  .copy--pink { color: var(--magenta); }

  .heading {
    position: absolute;
    font-family: "Montserrat", sans-serif;
    font-weight: 700;
    font-size: 11px;
    letter-spacing: 0.2px;
    z-index: 1;
  }
  .heading--pink { color: var(--magenta); }
  .heading--light { color: var(--white); }

  .decor { position: absolute; border-radius: 50%; }

  .social {
    position: absolute;
    left: 48px;
    display: flex;
    align-items: center;
    gap: 12px;
    font-size: 9.5px;
    font-weight: 600;
    color: var(--ink);
    z-index: 1;
  }
  .social__icon {
    width: 26px; height: 26px; border-radius: 50%;
    flex: none;
  }
  .social__icon--a { background: #3b5a9a; }
  .social__icon--b { background: #2d4a86; }
  .social__icon--c { background: #e0262c; }
  .social__icon--d { background: #e8578c; }
</style>
</head>
<body>

<section class="page page--front">
  <svg class="shape" viewBox="0 0 492 695" preserveAspectRatio="none" aria-hidden="true">
    <path d="M0 75 Q246 269 492 75 L492 332 L0 332 Z" fill="var(--magenta)"/>
    <rect x="0" y="297" width="204" height="35" fill="var(--white)"/>
    <rect x="329" y="418" width="163" height="34" fill="var(--magenta)"/>
    <path d="M0 452 L492 452 L492 695 Q246 575 0 695 Z" fill="var(--magenta)"/>
  </svg>

  <div class="brand" style="top:26px;"><span class="brand__dot"></span>Brisk Plumes</div>

  <div class="decor" role="img" aria-label="Speckled decorative splash" style="left:412px;top:218px;width:60px;height:88px;background:var(--faint-on-pink);"></div>
  <div class="decor" role="img" aria-label="Faint brand mark decoration" style="left:8px;top:330px;width:64px;height:96px;background:var(--faint);"></div>
  <div class="decor" role="img" aria-label="Speckled decorative splash" style="left:420px;top:455px;width:60px;height:90px;background:var(--faint-on-pink);"></div>
  <div class="decor" role="img" aria-label="Faint brand mark decoration" style="left:128px;top:592px;width:54px;height:86px;background:var(--faint);"></div>
  <div class="decor" role="img" aria-label="Faint brand mark decoration" style="left:218px;top:592px;width:54px;height:86px;background:var(--faint);"></div>
  <div class="decor" role="img" aria-label="Faint brand mark decoration" style="left:310px;top:592px;width:54px;height:86px;background:var(--faint);"></div>

  <div class="copy copy--light" style="left:48px;top:166px;width:390px;">
    <p>"Brisk Plumes</p>
    <p>Unlike many other extraction processes, our oil is SOLVENT-FREE with absolutely NO additives or harmful chemicals. All of our extractions are strain specific and lab tested for potency, residuals, and most importantly CONSISTENCY.</p>
    <p>Our vapes are specifically designed to be discreet yet incredibly effective for everyday use.</p>
    <p>It's simple. NO butane, NO glycol, NO glycerin. Just pure cannabis oil made in California"</p>
    <p>"Voted Best Oil at 2015 Leafmoot in San Bernardino and San Francisco"</p>
  </div>

  <h2 class="heading heading--pink" style="left:47px;top:309px;">KNOW THE DIFFERENCE</h2>
  <div class="copy copy--pink" style="left:47px;top:350px;width:400px;">
    <p>Butane is a highly volatile and flammable gas used for cannabis extractions also known as "BHO" extractions very popular in today's industry. These extractions are not only dangerous, but also contain chemical contaminants that could present health hazards and cause harmful nodules in the lungs that increase chances of getting infections. When done improperly, harmful chemical solvents are left over for the consumers to smoke, which can cause detrimental long-term health effects.</p>
  </div>

  <h2 class="heading heading--light" style="left:361px;top:429px;">WHAT IS THC?</h2>
  <div class="copy copy--light" style="left:45px;top:468px;width:390px;height:90px;overflow:hidden;">
    <p>THC, or "tetrahydrocannabinol," is the chemical responsible for most of marijuana's psychological effects. It acts much like the cannabinoid chemicals made naturally by the body.</p>
    <p>Cannabinoid receptors are concentrated in certain areas of the brain associated with thinking, memory, pleasure, coordination, and time perception. THC attaches to these receptors and activates them.</p>
    <p>THC is one of many compounds found in the resin secreted by glands of the marijuana plant. More of these glands are found around the reproductive organs of the plant than on any other</p>
  </div>
</section>

<section class="page page--back">
  <svg class="shape" viewBox="0 0 494 697" preserveAspectRatio="none" aria-hidden="true">
    <path d="M0 55 Q247 249 494 55 L494 337 L289 337 L289 373 L0 373 Z" fill="var(--magenta)"/>
    <rect x="0" y="197" width="204" height="40" fill="var(--white)"/>
    <rect x="0" y="469" width="494" height="18" fill="var(--magenta)"/>
    <rect x="0" y="673" width="494" height="24" fill="var(--magenta)"/>
  </svg>

  <div class="brand" style="top:30px;"><span class="brand__dot"></span>Brisk Plumes</div>

  <div class="decor" role="img" aria-label="Speckled decorative splash" style="left:418px;top:215px;width:60px;height:90px;background:var(--faint-on-pink);"></div>
  <div class="decor" role="img" aria-label="Speckled decorative splash" style="left:18px;top:255px;width:40px;height:70px;background:var(--faint-on-pink);"></div>
  <div class="decor" role="img" aria-label="Faint brand mark decoration" style="left:412px;top:356px;width:72px;height:106px;background:var(--faint);"></div>
  <div class="decor" role="img" aria-label="Faint brand mark decoration" style="left:122px;top:590px;width:64px;height:86px;background:var(--faint);"></div>
  <div class="decor" role="img" aria-label="Faint brand mark decoration" style="left:215px;top:590px;width:64px;height:86px;background:var(--faint);"></div>
  <div class="decor" role="img" aria-label="Faint brand mark decoration" style="left:307px;top:590px;width:64px;height:86px;background:var(--faint);"></div>

  <h2 class="heading heading--pink" style="left:46px;top:210px;">WHAT IS CBD?</h2>
  <div class="copy copy--light" style="left:48px;top:250px;width:416px;">
    <p>CBD is one of over 60 compounds found in cannabis that belongs to a class of molecules called "cannabinoids." CBD from cannabis is non-psychoactive or less psychoactive than THC-dominant strains, making it an appealing option for patients looking for relief from inflammation, pain, anxiety, psychosis, seizures, spasms, and other conditions without disconcerting feelings of lethargy</p>
    <p>or dysphoria. CBD has demonstrable neuroprotective and neurogenic effects, and its anti-cancer properties are currently being investigated at several academic research centers in the United States and elsewhere."</p>
  </div>

  <div class="copy copy--pink" style="left:45px;top:385px;width:370px;">
    <p>"Cleaning &amp; Care</p>
    <p>Store vape cartridges flat or upright in cool or room temperature to prevent leakage. Exposure to excessive heat may cause the viscosity of the oil to change.</p>
    <p>Please refer to our Clipstream (https://lnk.example-short.test/Qp7RmZ) page for videos on proper storage and refill instructions!</p>
  </div>

  <div class="social" style="top:509px;"><span class="social__icon social__icon--a"></span>BriskPlume_</div>
  <div class="social" style="top:545px;"><span class="social__icon social__icon--b"></span>BriskPlumesProducts</div>
  <div class="social" style="top:579px;"><span class="social__icon social__icon--c"></span>Brisk Plume (https://lnk.example-short.test/Qp7RmZ)</div>
  <div class="social" style="top:616px;"><span class="social__icon social__icon--d"></span>contact@briskplume-mail.test</div>
</section>

</body>
</html>
```